Bluestone Advisory & Mgmt - Professional Business Cards

Hi!

I am a Real Estate Developer and Construction Consultant.

I have a lot of inspiration from previous designs and would be open to using the attached Designs as a starting point. I would like to see these styles incorporated into your designs.

I really need professional business card to go with it that includes my important info.

Look forward to seeing your designs!.

Target Market(s)

My Target market are building owners, lawyers, consultants.

Industry/Entity Type

Real Estate Development

Contact Information for Business Card

My Name: Dorian Pelkey
My Title: Principle
Company Name: Bluestone Advisory & Mgmt, LLC
Address: 348 West 71st Street, 9th FL New York, NY 10010
Mobile: 917.806.3971
Website: bam-hvx.example

Font styles to use
Serif
Sans Serif

Colors

Designer to choose colors to be used in the design.

Requirements
Must have
• Must incorporate the logo attached or have new that looks similar.
• Must use professional font that will be seen and judged by wealthy land owners and developers.
• Must incorporate some of the color green.
Should not have
• Photo's or pictures of people or buildings of any kind.

```html
<!DOCTYPE html>
<html lang="en">
<head>
<meta charset="utf-8">
<title>Bluestone Advisory &amp; Mgmt - Business Cards</title>
<link rel="stylesheet" href="https://fonts.googleapis.com/css2?family=Raleway:wght@400&family=Open+Sans:wght@400;700&display=swap">
<style>
  :root{
    --bg:#1c1c1c;
    --paper:#ffffff;
    --green:#50b87c;
    --grey:#948d8c;
    --grey-dark:#858080;
    --ink-light:#ffffff;
  }
  *{margin:0;padding:0;box-sizing:border-box;}
  html,body{width:1200px;height:1106px;overflow:hidden;background:var(--bg);}
  .canvas{position:relative;width:1200px;height:1106px;}
  .card{position:absolute;left:220px;width:760px;height:434px;background:var(--paper);overflow:hidden;}
  .card--front{top:90px;}
  .card--back{top:582px;}

  .brand{position:absolute;font-family:"Raleway",sans-serif;font-weight:400;color:var(--green);line-height:1.1;}
  .card--front .brand{left:0;right:0;top:150px;text-align:center;font-size:46px;}
  .brand__mark{display:inline-block;width:22px;height:22px;background:var(--green);margin-right:14px;vertical-align:middle;position:relative;top:-4px;}
  .website{position:absolute;left:0;right:0;top:300px;text-align:center;font-family:"Open Sans",sans-serif;font-size:19px;letter-spacing:6px;color:var(--grey);}

  .card__shape{position:absolute;inset:0;width:760px;height:434px;}
  .card--back .brand{left:44px;top:175px;width:380px;font-size:36px;}
  .contact{position:absolute;right:36px;top:44px;text-align:right;font-family:"Open Sans",sans-serif;color:var(--ink-light);}
  .contact__name{font-weight:700;font-size:24px;text-transform:uppercase;letter-spacing:.5px;}
  .contact__title{font-weight:700;font-size:19px;margin-bottom:24px;}
  .contact__line{font-size:16px;line-height:1.55;display:flex;justify-content:flex-end;align-items:center;gap:8px;}
  .contact__line svg{width:14px;height:14px;flex:none;}
  .contact__address{margin-top:26px;font-size:16px;line-height:1.55;}
</style>
</head>
<body>
<main class="canvas">
  <section class="card card--front">
    <div class="brand"><span class="brand__mark"></span>Bluestone Advisory &amp; Mgmt</div>
    <p class="website">www.bam-hvx.example</p>
  </section>

  <section class="card card--back">
    <svg class="card__shape" viewBox="0 0 760 434" aria-hidden="true">
      <path d="M400,0 C500,90 480,300 480,434 L545,434 C530,300 560,110 470,0 Z" fill="var(--grey)"/>
      <path d="M470,0 C560,110 530,300 545,434 L760,434 L760,0 Z" fill="var(--green)"/>
    </svg>
    <div class="brand">Bluestone Advisory &amp; Mgmt</div>
    <div class="contact">
      <p class="contact__name">Dorian Pelkey</p>
      <p class="contact__title">Principle</p>
      <p class="contact__line">917.806.3971
        <svg viewBox="0 0 16 16"><circle cx="8" cy="8" r="7" fill="none" stroke="#fff" stroke-width="1.5"/><path d="M5.5 4.5l2 2-1 1c.6 1.2 1.3 1.9 2.5 2.5l1-1 2 2-1.2 1.2C8 12 4 8 4.3 5.7z" fill="#fff"/></svg></p>
      <p class="contact__line">office@bam-hvx.example
        <svg viewBox="0 0 16 16"><rect x="1.5" y="3.5" width="13" height="9" fill="none" stroke="#fff" stroke-width="1.5"/><path d="M1.5 3.5l6.5 5 6.5-5" fill="none" stroke="#fff" stroke-width="1.5"/></svg></p>
      <p class="contact__line">www.bam-hvx.example
        <svg viewBox="0 0 16 16"><circle cx="8" cy="8" r="6.5" fill="none" stroke="#fff" stroke-width="1.4"/><ellipse cx="8" cy="8" rx="3" ry="6.5" fill="none" stroke="#fff" stroke-width="1.2"/><path d="M1.5 8h13" stroke="#fff" stroke-width="1.2"/></svg></p>
      <p class="contact__address">348 West 71st Street<br>9th FL New York, NY 10010</p>
    </div>
  </section>
</main>
</body>
</html>
```